New Award Winning Plumbing Tool - enter and win promotion

We need an A3 poster that can go up onsite and stores and construction sites to increase LIKEs of our Chatterbook Page. Each LIKE goes into the draw to present the trophy and meet Miss Sunwave Coastal 2013. It must also highlight the product so that people will ask for it at their suppliers
Updates

Hi, thanks for the emails. Poster to be A3 please. 3rd logo removed as it is the Homegrown Quality logo and we cant use this for promotional purposes of this kind. Thanks

Target Market(s)

Tradesmen, aged 25-45 living in Victoria

Industry/Entity Type

Construction

Requirements
Must have
• Uploaded ALL pictures & logos
FOLLOWING TEXT
FLEXI-TURN Silicone Nozzles Presents/ Logo
Your chance to meet 'MISS SUNWAVE COASTAL 2013'
- present the winners trophy
- have a contestant deliver pizza and drinks to your worksite
LIKE our chatterbook page
*see our website www.flexiturnsiliconenozzles.example or chatterbook page for Terms and Conditions
Entries close 30 September 2013
Brought to you by the award winning World's First, Bendable, Extendable, Reusable Silicone Nozzle
Designed by an Aussie Plumber for Aussie Plumbers
Ask for us at BLANK BOX

Nice to have
• WIN symbol
ticks next to the prize information
MISS SUNWAVE in eye catching writing

```html
<!DOCTYPE html>
<html lang="en">
<head>
<meta charset="utf-8">
<title>Miss Sunwave Coastal 2013 – FLEXI-TURN Silicone Nozzles</title>
<link rel="stylesheet" href="https://fonts.googleapis.com/css2?family=Oswald:wght@500;700&family=Audiowide&family=Black+Ops+One&family=Lato:wght@400;700;900&display=swap">
<style>
:root{
  --bg-deep:#6e4350;
  --bg-mid:#b98a93;
  --bg-light:#f3dfe4;
  --pink:#e2307f;
  --pink-soft:#f29ac4;
  --blue:#2b5fb4;
  --red:#d3202a;
  --red-dark:#8f1218;
  --ink:#2a1a20;
  --white:#ffffff;
  --tick:#3bb02a;
  --band:#4a2c37;
  --steel-1:#ffffff;
  --steel-2:#c9b9bf;
  --steel-3:#5d4450;
}
*{box-sizing:border-box;margin:0;padding:0}
html,body{width:850px;height:1200px;overflow:hidden;background:var(--white)}
.poster{
  position:relative;width:850px;height:1200px;overflow:hidden;
  background:
    radial-gradient(ellipse 70% 30% at 50% 88%, rgba(255,255,255,.95), rgba(255,255,255,0) 70%),
    radial-gradient(ellipse 80% 60% at 55% 40%, var(--bg-light), var(--bg-mid) 60%, var(--bg-deep) 100%);
  font-family:'Lato',sans-serif;
}
.like-banner{
  position:absolute;left:-95px;top:55px;width:420px;height:92px;
  transform:rotate(-35deg);background:var(--white);
  border-top:7px solid var(--pink);border-bottom:7px solid var(--pink);
  display:flex;align-items:center;justify-content:center;gap:14px;
}
.like-banner .mark{width:34px;height:34px;background:var(--blue);border-radius:4px}
.like-banner .label{
  font-family:'Lato',sans-serif;font-weight:900;color:var(--blue);
  font-size:30px;line-height:1;text-align:center;
}
.brand-mark{
  position:absolute;left:325px;top:28px;width:170px;text-align:center;
}
.brand-mark .dot{
  width:70px;height:70px;border-radius:50%;margin:0 auto 8px;
  background:var(--blue);
}
.brand-mark .name{
  font-family:'Oswald',sans-serif;font-weight:500;color:var(--blue);
  font-size:19px;line-height:1.15;
}
.presenter{
  position:absolute;right:22px;top:70px;width:300px;text-align:center;color:var(--white);
}
.presenter .company{font-family:'Oswald',sans-serif;font-weight:700;font-size:40px;line-height:1}
.presenter .tagline{font-family:'Oswald',sans-serif;font-weight:500;font-size:22px;margin-top:6px}
.ribbon{
  position:absolute;right:0;top:158px;width:335px;height:36px;
  background:linear-gradient(var(--red),var(--red-dark));
  clip-path:polygon(18px 0,100% 0,100% 100%,18px 100%,0 50%);
  display:flex;align-items:center;justify-content:center;
  color:var(--white);font-size:16px;font-weight:700;
}
.hero-photo{
  position:absolute;left:90px;top:240px;width:720px;height:600px;
  background:
    radial-gradient(ellipse 60% 45% at 50% 45%, rgba(230,170,140,.75), rgba(230,170,140,0) 70%),
    linear-gradient(180deg, rgba(120,70,60,.35), rgba(240,140,200,.35) 70%, rgba(255,255,255,0));
  border-radius:40px 40px 0 0;
}
.entries{
  position:absolute;left:48px;top:628px;transform:rotate(-4deg);
  color:var(--white);text-align:center;font-family:'Oswald',sans-serif;font-weight:700;
}
.entries .top{background:var(--red);padding:2px 12px;font-size:30px;line-height:1.1;display:inline-block}
.entries .date{background:var(--ink);padding:0 14px;font-size:58px;line-height:1;display:block;margin-top:-2px}
.entries .month{background:var(--red);padding:2px 10px;font-size:24px;display:inline-block}
.chance{
  position:absolute;left:305px;top:768px;color:var(--ink);
  font-family:'Lato',sans-serif;font-weight:700;font-size:24px;
}
.title{
  position:absolute;left:0;top:800px;width:850px;text-align:center;
  font-family:'Audiowide',sans-serif;line-height:1;
  background:linear-gradient(180deg,var(--steel-1) 0%,var(--steel-2) 45%,var(--steel-3) 55%,var(--steel-2) 100%);
  -webkit-background-clip:text;background-clip:text;color:transparent;
  filter:drop-shadow(0 3px 2px rgba(40,20,30,.7));
}
.title .name{display:block;font-size:54px;letter-spacing:1px}
.title .year{display:block;font-size:66px;margin-top:4px}
.prizes{
  position:absolute;left:250px;top:968px;list-style:none;color:var(--ink);
  font-weight:700;font-size:23px;
}
.prizes li{display:flex;align-items:center;gap:12px;margin-bottom:8px}
.prizes li:first-child{margin-left:10px}
.prizes li:last-child{margin-left:-150px}
.prizes svg{width:30px;height:30px;flex:none}
.terms{
  position:absolute;left:0;top:1048px;width:850px;height:26px;background:var(--white);
  color:var(--blue);font-size:15px;display:flex;align-items:center;justify-content:center;
}
.terms b{font-weight:400;color:var(--pink)}
.footer{
  position:absolute;left:0;top:1076px;width:850px;height:124px;background:var(--band);
  color:var(--white);text-align:center;font-family:'Black Ops One',sans-serif;
  padding-top:12px;font-size:20px;line-height:1.2;
}
.ask{
  margin-top:12px;display:flex;justify-content:center;align-items:center;gap:14px;
  font-family:'Lato',sans-serif;color:var(--pink-soft);font-size:20px;
}
.ask .blank{width:170px;height:34px;background:var(--white)}
</style>
</head>
<body>
<main class="poster">
  <div class="hero-photo" role="img" aria-label="Photograph of three smiling contestants in pink bikinis against palm leaves"></div>

  <div class="like-banner"><span class="mark"></span><span class="label">like us on<br>chatterbook</span></div>

  <div class="brand-mark">
    <div class="dot"></div>
    <div class="name">FLEXI-TURN<br>Silicone Nozzles</div>
  </div>

  <div class="presenter">
    <div class="company">FLEXI-TURN</div>
    <div class="tagline">Silicone Nozzles Presents</div>
  </div>
  <div class="ribbon">www.flexiturnsiliconenozzles.example</div>

  <div class="entries">
    <span class="top">Entries close</span>
    <span class="date">30th</span>
    <span class="month">September 2013</span>
  </div>

  <p class="chance">Your chance to meet</p>
  <h1 class="title"><span class="name">MISS SUNWAVE COASTAL</span><span class="year">2013</span></h1>

  <ul class="prizes">
    <li><svg viewBox="0 0 30 30"><rect x="3" y="8" width="19" height="19" fill="none" stroke="#2a1a20" stroke-width="2.5"/><path d="M7 16l5 6L28 2" fill="none" stroke="#3bb02a" stroke-width="4" stroke-linecap="round"/></svg>present the winners trophy</li>
    <li><svg viewBox="0 0 30 30"><rect x="3" y="8" width="19" height="19" fill="none" stroke="#2a1a20" stroke-width="2.5"/><path d="M7 16l5 6L28 2" fill="none" stroke="#3bb02a" stroke-width="4" stroke-linecap="round"/></svg>have a contestant deliver pizza and drinks to your worksite</li>
  </ul>

  <p class="terms">see our website&nbsp;<b>www.flexiturnsiliconenozzles.example</b>&nbsp;or chatterbook page for Terms and Conditions</p>

  <footer class="footer">
    brought to you by the award winning world's first,bendable,extendable,reusable silicone nozzle<br>
    designed by an aussie plumber for aussie plumbers
    <div class="ask">Ask for us at <span class="blank"></span></div>
  </footer>
</main>
</body>
</html>
```